Harrowby Lending Hard Money Lender

We are looking for this flyer to be redesigned. We would like it to be even more simple than the attached design. No photos, no exclamation points, a 3-4 color palate maximum. We would do not want any graphics around the "Harrowby Lending" logo.

```html
<!DOCTYPE html>
<html lang="en">
<head>
<meta charset="utf-8">
<title>Harrowby Lending – Hard Money Loans</title>
<link href="https://fonts.googleapis.com/css2?family=Lato:ital,wght@0,400;0,700;1,400&display=swap" rel="stylesheet">
<style>
  :root {
    --navy: #062a3d;
    --white: #ffffff;
  }
  html, body {
    margin: 0;
    padding: 0;
    overflow: hidden;
    background: var(--navy);
  }
  .flyer {
    position: relative;
    width: 927px;
    height: 1200px;
    background: var(--navy);
    color: var(--white);
    font-family: "Lato", Arial, sans-serif;
    overflow: hidden;
  }
  .flyer > * {
    position: absolute;
    margin: 0;
    line-height: 1;
  }
  .accent-bar {
    background: var(--white);
    width: 20px;
  }
  .accent-bar--headline { left: 106px; top: 302px; height: 224px; }
  .accent-bar--services { left: 478px; top: 547px; height: 148px; }
  .accent-bar--benefits { left: 106px; top: 772px; height: 157px; }
  .accent-bar--contact  { left: 800px; top: 1005px; height: 157px; }

  .brand-name {
    left: 0;
    width: 834px;
    top: 98px;
    text-align: center;
    font-weight: 400;
    font-size: 46px;
    letter-spacing: 3px;
  }
  .headline {
    left: 145px;
    top: 306px;
    font-weight: 700;
    font-size: 66px;
    letter-spacing: 1px;
  }
  .rate-note {
    left: 148px;
    top: 497px;
    font-style: italic;
    font-size: 22px;
    letter-spacing: 0.5px;
  }
  .service-list {
    left: 511px;
    top: 550px;
    list-style: none;
    padding: 0;
    font-weight: 700;
    font-size: 36px;
  }
  .service-list li { line-height: 55px; }

  .benefit-list {
    left: 141px;
    top: 775px;
    list-style: none;
    padding: 0;
    font-weight: 700;
    font-size: 21px;
  }
  .benefit-list li { line-height: 32px; }
  .benefit-list small { font-size: 14px; font-weight: 400; }

  .phone {
    left: 138px;
    top: 870px;
    font-weight: 700;
    font-size: 64px;
    letter-spacing: 0.5px;
  }
  .contact-email,
  .contact-web {
    left: 106px;
    font-weight: 700;
    font-size: 25px;
  }
  .contact-email { top: 1023px; }
  .contact-web   { top: 1066px; }
  .contact-address {
    left: 106px;
    top: 1117px;
    font-weight: 700;
    font-size: 17px;
    white-space: pre;
  }
</style>
</head>
<body>
  <main class="flyer">
    <p class="brand-name">HARROWBY LENDING</p>

    <div class="accent-bar accent-bar--headline"></div>
    <h1 class="headline">HARD MONEY LOANS</h1>
    <p class="rate-note">Rates From 8%</p>

    <div class="accent-bar accent-bar--services"></div>
    <ul class="service-list">
      <li>Fix &amp; Flip Loans</li>
      <li>Commercial Loans</li>
      <li>Hard Money Loans</li>
    </ul>

    <div class="accent-bar accent-bar--benefits"></div>
    <ul class="benefit-list">
      <li>Same-Day Approval</li>
      <li>No Processing, Appraisal, or Extra Fees</li>
      <li>100% Financing <small>(w/ Additional Collateral)</small></li>
    </ul>
    <p class="phone">303.555.0147</p>

    <p class="contact-email">harrowby802@mail.com</p>
    <p class="contact-web">http://harrowbylending.com</p>
    <p class="contact-address">1480 Meadowlark Ave., Suite 200   Denver, CO 80231</p>
    <div class="accent-bar accent-bar--contact"></div>
  </main>
</body>
</html>
```